A Brochure to sell LED Downlights to clients

I am starting a campaign on zestoria for LED down lights the link to the landing page can be found at brindlemoss.com.au/led .

When the client send a contact request i want to be able to send back a brochure of a picture of each light (Approx 6 - 8 types) and have a few sentences on each light and price brake down.

'Quarnil Sabeto 9w LED'

**Information**

1-10 lights $49
11-20 lights $45
21 - 40 lights $42
40 and over $40

EACH LIGHT:

Hi,

This is very good.

I
But,

Each light will have its own price.

Can i get it made like this;

Picture - Spec - Pricing in a table style please? - i like the layout it just need to suit the tables under:

picture - Brand - Price 1-10
Model - Price 11-20
Watts - Price 21-21
lumen - price 30- 40
Warranty = price 40+

Model - Price 11-20
Watts - Price 21-21
lumen - price 30- 40
Warranty = price 40+

Model - Price 11-20
Watts - Price 21-21
lumen - price 30- 40
Warranty = price 40+

and so on....

I want it to be on Microsoft Word so i can easily chop and edit the prices and images also. (So i can print to PDF)

For more information see my website to seek inspiration. I have a zip file of my logo for actual creation and should be also to source pictures of the lights when finalising the design.

brindlemoss.com.au

Thanks

Target Market(s)

Homeowners/commercial business owners

Industry/Entity Type

Electric Company

Font styles to use
Sans Serif

Colors
86cfc6
ffffff
000000

Requirements
Must have
• Professional looking, Colours to the theme of my logo/website
Nice to have
• An awesome design that sells it's self!!!!!!!
• My Logo font is 'Radikil" it would be nice to follow that theme if it doesn't look good i am open to have a nice legible font for the copy.
Should not have
• Cheesy light globes or images

```html
<!DOCTYPE html>
<html lang="en">
<head>
<meta charset="utf-8">
<title>Brindlemoss Electrical – LED Downlight Brochure</title>
<link href="https://fonts.googleapis.com/css2?family=Montserrat:wght@400;500;600;700;800&display=swap" rel="stylesheet">
<style>
  :root{
    --teal:#1aa99a;
    --teal-soft:#86cfc6;
    --teal-deep:#11877b;
    --ink:#2b2b2b;
    --ink-soft:#4a4a4a;
    --paper:#e9e9e9;
    --paper-light:#f4f4f4;
    --band:#555759;
    --white:#ffffff;
  }
  *{box-sizing:border-box;margin:0;padding:0}
  html,body{width:1200px;height:847px;overflow:hidden;background:var(--paper)}
  body{font-family:"Montserrat",Arial,sans-serif;color:var(--ink)}
  .spread{position:relative;width:1200px;height:847px;overflow:hidden;background:var(--paper-light)}
  .spread__art{position:absolute;inset:0}
  .fold{position:absolute;left:600px;top:0;width:1px;height:847px;background:rgba(0,0,0,.08)}

  .product{position:absolute;left:40px;top:338px;width:520px;height:116px;display:flex;gap:14px;padding:10px;background:rgba(255,255,255,.85);border-left:4px solid var(--teal)}
  .product__photo{flex:none;width:92px;height:96px}
  .product__name{font-size:12px;font-weight:700;color:var(--teal);margin-bottom:4px;letter-spacing:.3px}
  .product__body{flex:1}
  .product__tables{display:flex;gap:14px}
  .spec-table,.price-table{border-collapse:collapse;font-size:10.5px}
  .spec-table{width:170px}
  .price-table{width:200px}
  .spec-table th,.price-table th{text-align:left;font-weight:600;color:var(--ink-soft);padding:1.5px 6px 1.5px 0}
  .spec-table td,.price-table td{font-weight:500;color:var(--ink);padding:1.5px 0}
  .spec-table tr,.price-table tr{border-bottom:1px solid #dcdcdc}
  .price-table td{text-align:right;color:var(--teal-deep);font-weight:700}

  .welcome{position:absolute;left:44px;top:470px}
  .welcome__lead{font-size:36px;font-weight:800;color:var(--teal);line-height:1}
  .welcome__company{font-size:24px;font-weight:700;color:var(--ink);margin-top:6px;letter-spacing:.5px}
  .welcome__rule{width:120px;height:5px;background:var(--teal);margin:10px 0 8px}
  .welcome__tagline{font-size:15px;font-weight:500;color:var(--ink-soft);line-height:1.35}

  .brand{position:absolute;left:50px;top:700px;display:flex;align-items:center;gap:10px}
  .brand__mark{width:14px;height:14px;background:var(--teal)}
  .brand__name{font-size:34px;font-weight:600;color:var(--teal);letter-spacing:-.5px}

  .contact-divider{position:absolute;left:300px;top:650px;width:2px;height:150px;background:var(--teal)}
  .contact{position:absolute;left:330px;top:648px}
  .contact__title{font-size:21px;font-weight:500;color:var(--ink);margin-bottom:16px;letter-spacing:.5px}
  .contact__row{display:flex;align-items:center;gap:12px;font-size:14px;font-weight:500;color:var(--ink);margin-bottom:12px}
  .contact__row svg{width:18px;height:18px;flex:none}

  .photo-brand{position:absolute;right:60px;top:38px;font-size:28px;font-weight:600;color:var(--white);display:flex;align-items:center;gap:8px}
  .photo-brand__mark{width:10px;height:10px;background:var(--white)}

  .pitch{position:absolute;left:660px;top:548px}
  .pitch__lead{font-size:24px;font-weight:700;color:var(--ink);letter-spacing:.3px}
  .pitch__headline{font-size:40px;font-weight:800;color:var(--teal);line-height:1.05;margin-top:4px}
  .pitch__close{font-size:17px;font-weight:700;color:var(--ink);margin-top:6px;letter-spacing:.2px}
  .pitch__url{display:inline-block;margin-top:30px;padding:10px 30px;border-radius:22px;background:var(--teal);color:var(--white);font-size:17px;font-weight:500;letter-spacing:4px;box-shadow:0 3px 0 var(--teal-deep)}
</style>
</head>
<body>
<main class="spread">
  <svg class="spread__art" width="1200" height="847" viewBox="0 0 1200 847">
    <defs>
      <linearGradient id="buildingTone" x1="0" y1="0" x2="0" y2="1">
        <stop offset="0" stop-color="#cfcfcf"/>
        <stop offset="1" stop-color="#f0f0f0"/>
      </linearGradient>
      <linearGradient id="vanTone" x1="0" y1="0" x2="1" y2="1">
        <stop offset="0" stop-color="#2fb8a9"/>
        <stop offset="1" stop-color="#158f83"/>
      </linearGradient>
      <linearGradient id="interiorTone" x1="0" y1="0" x2="1" y2="1">
        <stop offset="0" stop-color="#d6b25a"/>
        <stop offset=".55" stop-color="#a67a3a"/>
        <stop offset="1" stop-color="#5b3f22"/>
      </linearGradient>
    </defs>
    <rect class="photo photo--building" x="0" y="60" width="600" height="560" fill="url(#buildingTone)" opacity=".75" role="img" aria-label="Faded greyscale photo of a brick building entrance"/>
    <rect x="0" y="520" width="600" height="327" fill="var(--paper-light)" opacity=".55"/>
    <polygon class="photo photo--van" points="0,0 800,0 655,265 600,300 0,36" fill="url(#vanTone)" role="img" aria-label="Teal-tinted photo of a company service van"/>
    <polygon class="band" points="0,36 600,300 655,265 665,282 600,330 0,62" fill="var(--band)"/>
    <polygon class="photo-frame" points="800,0 1200,0 1200,648 640,300" fill="var(--white)"/>
    <polygon class="photo photo--interior" points="812,0 1200,0 1200,632 656,300" fill="url(#interiorTone)" role="img" aria-label="Photo of a warmly lit restaurant interior with diners"/>
  </svg>
  <div class="fold"></div>

  <section class="product">
    <svg class="product__photo" viewBox="0 0 92 96" role="img" aria-label="Product photo of the Quarnil Sabeto 9w LED downlight">
      <defs>
        <radialGradient id="lightTone" cx=".5" cy=".45" r=".6">
          <stop offset="0" stop-color="#ffffff"/>
          <stop offset="1" stop-color="#c9cfce"/>
        </radialGradient>
      </defs>
      <rect width="92" height="96" fill="url(#lightTone)"/>
    </svg>
    <div class="product__body">
      <h2 class="product__name">QUARNIL SABETO 9W LED</h2>
      <div class="product__tables">
        <table class="spec-table">
          <tr><th>Brand</th><td>Quarnil</td></tr>
          <tr><th>Model</th><td>Sabeto</td></tr>
          <tr><th>Watts</th><td>9w</td></tr>
          <tr><th>Lumen</th><td>TBC</td></tr>
          <tr><th>Warranty</th><td>TBC</td></tr>
        </table>
        <table class="price-table">
          <tr><th>1 – 10 lights</th><td>$49</td></tr>
          <tr><th>11 – 20 lights</th><td>$45</td></tr>
          <tr><th>21 – 40 lights</th><td>$42</td></tr>
          <tr><th>40 and over</th><td>$40</td></tr>
        </table>
      </div>
    </div>
  </section>

  <section class="welcome">
    <p class="welcome__lead">Welcome to</p>
    <p class="welcome__company">BRINDLEMOSS PTY LTD</p>
    <div class="welcome__rule"></div>
    <p class="welcome__tagline">Providing White Collar Professionalism<br>in A Blue Collar Industry</p>
  </section>

  <div class="brand">
    <span class="brand__mark"></span>
    <span class="brand__name">brindlemoss</span>
  </div>

  <div class="contact-divider"></div>
  <section class="contact">
    <h2 class="contact__title">CONTACT US</h2>
    <p class="contact__row">
      <svg viewBox="0 0 18 18"><rect x="5" y="1" width="8" height="16" rx="1.5" fill="none" stroke="var(--teal)" stroke-width="1.6"/><circle cx="9" cy="14" r="1" fill="var(--teal)"/></svg>
      0400 555 019
    </p>
    <p class="contact__row">
      <svg viewBox="0 0 18 18"><circle cx="9" cy="9" r="7" fill="none" stroke="var(--teal)" stroke-width="1.6"/><path d="M2 9h14M9 2c3 3 3 11 0 14M9 2c-3 3-3 11 0 14" fill="none" stroke="var(--teal)" stroke-width="1.2"/></svg>
      brindlemoss.com.au
    </p>
    <p class="contact__row">
      <svg viewBox="0 0 18 18"><rect x="1.5" y="4" width="15" height="10" rx="1" fill="none" stroke="var(--teal)" stroke-width="1.6"/><path d="M2 5l7 5 7-5" fill="none" stroke="var(--teal)" stroke-width="1.4"/></svg>
      info@brindlemoss.com.au
    </p>
  </section>

  <div class="photo-brand">
    <span class="photo-brand__mark"></span>
    <span>brindlemoss</span>
  </div>

  <section class="pitch">
    <p class="pitch__lead">WE RESPECT</p>
    <h1 class="pitch__headline">YOUR HOME &amp;<br>WORKPLACE</h1>
    <p class="pitch__close">AND TREAT IT ACCORDINGLY</p>
    <span class="pitch__url">www.brindlemoss.com.au</span>
  </section>
</main>
</body>
</html>
```